Urban Music Nightclub DJ Flyer

The flyer is for a night at a San Diego bar called Velvet & Tide. We tend to play V&T that is more on the bassier side of things but still accessible to the ladies.

The flyer colors would be predominately in black and gold. We're going for a slightly sultry look.

- Ornate Gold frame around the picture.

Changes to the picture:

- Supplied photo has an undesirable tile background
- make it grayscale.

The fonts should complement the frame, have a bit of texture and depth.

Flyer should read

V&T (Largest font)
presents (smallest font)
T DELANO (Large Font)
FRAZOL x MONDRIK (smaller font)

We've included a quick mock up.

We thank you for the many designs that were submitted. We are close to making our final decision.

```html
<!DOCTYPE html>
<html lang="en">
<head>
<meta charset="utf-8">
<title>V&amp;T presents T Delano</title>
<link rel="stylesheet" href="https://fonts.googleapis.com/css2?family=Bree+Serif&family=Josefin+Sans:wght@600&display=swap">
<style>
  :root {
    --gold-light: #f6b03c;
    --gold-mid: #e59a2a;
    --gold-deep: #b86e16;
    --frame-edge: #7a4a10;
    --night-top: #0f3350;
    --night-mid: #0b2740;
    --night-low: #06152a;
    --title-gold: #f5bb22;
    --rose: #e07c8e;
  }
  * { margin: 0; padding: 0; box-sizing: border-box; }
  html, body {
    width: 800px; height: 1200px; overflow: hidden;
    background: var(--gold-mid);
  }
  .flyer {
    position: relative;
    width: 800px; height: 1200px;
    background:
      linear-gradient(135deg, var(--gold-light) 0%, var(--gold-deep) 25%, var(--gold-light) 50%, var(--gold-deep) 75%, var(--gold-light) 100%);
  }
  .frame-inner {
    position: absolute;
    left: 42px; top: 42px; right: 42px; bottom: 42px;
    background: linear-gradient(315deg, var(--gold-light), var(--gold-deep) 50%, var(--gold-light));
    border: 2px solid var(--frame-edge);
  }
  .scene {
    position: absolute;
    left: 56px; top: 56px; right: 56px; bottom: 56px;
    border: 2px solid var(--frame-edge);
    background: linear-gradient(180deg, var(--night-top) 0%, var(--night-mid) 55%, var(--night-low) 100%);
    overflow: hidden;
  }
  .scene-photo {
    position: absolute; left: 0; top: 0; width: 100%; height: 100%;
  }
  .lockup {
    position: absolute; left: 0; top: 0; width: 100%; height: 100%;
  }
  .title {
    position: absolute; left: 36px; top: 590px;
    font-family: "Bree Serif", serif;
    font-size: 296px; line-height: 1;
    color: var(--title-gold);
    letter-spacing: 2px;
  }
  .presents {
    position: absolute; left: 49px; top: 878px;
    font-family: "Josefin Sans", sans-serif;
    font-size: 17px; color: var(--rose);
  }
  .headliner {
    position: absolute; left: 48px; top: 936px;
    font-family: "Bree Serif", serif;
    font-size: 76px; line-height: 1;
    color: var(--title-gold);
    letter-spacing: 2px;
  }
  .support {
    position: absolute; left: 50px; top: 1012px;
    font-family: "Josefin Sans", sans-serif;
    font-weight: 600;
    font-size: 31px; line-height: 1;
    color: var(--rose);
    letter-spacing: 1px;
  }
</style>
</head>
<body>
  <div class="flyer">
    <div class="frame-inner"></div>
    <div class="scene">
      <svg class="scene-photo" viewBox="0 0 688 1088" role="img" aria-label="Photo of the headliner lying back on a patterned pillow, arms over head, in a white tank top, set against a starry night sky">
        <defs>
          <linearGradient id="personTone" x1="0" y1="0" x2="1" y2="0">
            <stop offset="0" stop-color="#8a7a72"/>
            <stop offset="0.5" stop-color="#b8a49a"/>
            <stop offset="1" stop-color="#e9e9ea"/>
          </linearGradient>
        </defs>
        <rect x="80" y="85" width="608" height="470" rx="40" fill="url(#personTone)" opacity="0.85"/>
      </svg>
      <div class="lockup">
        <div class="title">V&amp;T</div>
        <div class="presents">presents</div>
        <div class="headliner">T DELANO</div>
        <div class="support">FRAZOL &amp; MONDRIK</div>
      </div>
    </div>
  </div>
</body>
</html>
```